Business Card Design

I need a business card for my baking business. Name of the company is Baked by Maren. I specialize in cookies and pies.
I don't make cupcakes or cakes. I would like a design with colors of brown, light pink and dark pink and maybe have the half eaten cookie be the dot of the "I" in my name. (Half eaten chocolate chip and the chips being hot pink light pink and brown chips).. I would like the card fun and modern design.
On the back of the card tag line- let me bake your day

Industry/Entity Type

Business

Contact Information for Business Card

Maren Dulwitch
Cell 5550193827
Email-Marendul27@ovenpost.net

```html
<!DOCTYPE html>
<html lang="en">
<head>
<meta charset="UTF-8">
<title>Baked by Maren — Business Card</title>
<link rel="stylesheet" href="https://fonts.googleapis.com/css2?family=Pinyon+Script&family=Open+Sans:wght@400;600&display=swap">
<style>
  :root {
    --stage: #0d0d0d;
    --cream: #fdf7f6;
    --blush: #f3d9db;
    --cocoa: #4a2c19;
    --cocoa-deep: #3a2212;
    --caramel: #b9753e;
    --ink: #7a5a45;
    --ink-dark: #4b2e1f;
    --tan: #e6c7a2;
    --cookie-light: #c98b4f;
    --cookie-dark: #6b3f22;
  }
  * { margin: 0; padding: 0; box-sizing: border-box; }
  html, body { width: 1200px; height: 1200px; overflow: hidden; }
  body { background: var(--stage); position: relative; font-family: "Open Sans", sans-serif; }

  .card-slot { position: absolute; top: 448px; width: 535px; height: 304px; }
  .card-slot.front-slot { left: 45px; }
  .card-slot.back-slot { left: 620px; }

  .card {
    position: absolute; top: 0; left: 0;
    width: 396px; height: 225px;
    transform: scale(1.351);
    transform-origin: 0 0;
    overflow: hidden;
    background: linear-gradient(110deg, var(--blush) 0%, var(--cream) 45%, #ffffff 100%);
  }
  .card-shapes { position: absolute; inset: 0; width: 396px; height: 225px; }

  .owner-name {
    position: absolute;
    font-family: "Pinyon Script", cursive;
    font-size: 23px;
    color: var(--ink);
    white-space: nowrap;
    letter-spacing: 0.5px;
  }
  .designation {
    position: absolute; left: 42px; top: 98px;
    font-size: 10px; font-weight: 600; color: var(--ink);
  }
  .cookie-photo {
    position: absolute;
    border-radius: 45% 50% 40% 48%;
    background: radial-gradient(circle at 35% 40%, var(--cookie-light) 0%, #a8683a 55%, var(--cookie-dark) 100%);
  }
  .contact {
    position: absolute;
    display: flex; align-items: center; gap: 6px;
    font-size: 8px; color: var(--tan); white-space: nowrap;
  }
  .contact svg { width: 9px; height: 9px; flex: none; }

  .name-rule { position: absolute; left: 40px; top: 102px; width: 260px; height: 1px; background: var(--ink); opacity: .7; }
  .specialties { position: absolute; left: 42px; top: 110px; width: 98px; list-style: none; }
  .specialties li {
    font-size: 8px; font-weight: 600; color: var(--ink-dark);
    height: 18.5px; line-height: 18px;
    border-bottom: 1px solid rgba(122, 90, 69, .25);
  }
  .specialties li:last-child { border-bottom: none; }
</style>
</head>
<body>

<!-- Front -->
<div class="card-slot front-slot">
  <div class="card card-front">
    <svg class="card-shapes" viewBox="0 0 396 225" aria-hidden="true">
      <path d="M0 152 C 110 140, 230 122, 396 150 L396 225 L0 225 Z" fill="var(--caramel)"/>
      <path d="M0 155 C 110 143, 230 125, 396 153 L396 225 L0 225 Z" fill="var(--cocoa)"/>
    </svg>
    <div class="owner-name" style="left:40px; top:66px;">Maren Dulwitch</div>
    <div class="designation">designation</div>
    <div class="cookie-photo" role="img" aria-label="Photo of stacked chocolate chip cookies" style="left:240px; top:45px; width:112px; height:62px;"></div>

    <div class="contact" style="left:20px; top:200px;">
      <svg viewBox="0 0 10 10"><rect x="0.5" y="2" width="9" height="6.5" fill="var(--tan)"/><path d="M0.5 2 L5 6 L9.5 2" fill="none" stroke="var(--cocoa)" stroke-width="0.9"/></svg>
      Marendul27@ovenpost.net
    </div>
    <div class="contact" style="left:260px; top:182px;">
      <svg viewBox="0 0 10 10"><path d="M2 1 L4 1 L4.6 3.4 L3.4 4.3 C4 5.6 4.6 6.2 5.8 6.7 L6.7 5.5 L9 6.1 L9 8.2 C5 8.6 1.5 5 1.8 1 Z" fill="var(--tan)"/></svg>
      5550193827
    </div>
    <div class="contact" style="left:260px; top:197px;">
      <svg viewBox="0 0 10 10"><circle cx="5" cy="5" r="4.3" fill="none" stroke="var(--tan)" stroke-width="1"/><ellipse cx="5" cy="5" rx="1.8" ry="4.3" fill="none" stroke="var(--tan)" stroke-width="0.8"/><path d="M0.8 5 H9.2" stroke="var(--tan)" stroke-width="0.8"/></svg>
      www.bakedbymaren.com
    </div>
  </div>
</div>

<!-- Back -->
<div class="card-slot back-slot">
  <div class="card card-back">
    <svg class="card-shapes" viewBox="0 0 396 225" aria-hidden="true">
      <path d="M0 0 H396 V48 C 320 30, 260 5, 160 22 C 90 34, 40 52, 0 50 Z" fill="var(--caramel)"/>
      <path d="M0 0 H396 V45 C 320 27, 260 2, 160 19 C 90 31, 40 49, 0 47 Z" fill="var(--cocoa-deep)"/>
      <path d="M0 180 C 70 215, 200 222, 396 178 L396 225 L0 225 Z" fill="var(--caramel)"/>
      <path d="M0 183 C 70 218, 200 225, 396 181 L396 225 L0 225 Z" fill="var(--cocoa)"/>
    </svg>
    <div class="owner-name" style="left:42px; top:68px;">Maren Dulwitch</div>
    <div class="name-rule"></div>
    <ul class="specialties">
      <li>Cookies</li>
      <li>Pies</li>
      <li>Chocolate Chip</li>
      <li>Chips Being</li>
    </ul>
    <div class="cookie-photo" role="img" aria-label="Photo of stacked chocolate chip cookies" style="left:262px; top:128px; width:112px; height:56px;"></div>
  </div>
</div>

</body>
</html>
```